Harbourline Homes Business Card Design

We need a business card for an established builder of high quality bespoke homes in Auckland and Northland. We build and renovate homes collaboratively facilitating effective communication between owners, builders, architects, suppliers and tradespeople. We have never built or renovated a home that leaks or has faults. We only use reliable materials. We have never been sued or had legal action taken against us. We are honest builders of bespoke homes not group mass produced homes. Our niche market is in character homes. We practice sustainability and have built a lot of coastal property. We have been in business for over thirty years . We would like to see natural colors of the environment sand,sea and maybe vegetation . The design should communicate quality, sustainability,fair pricing, open communication and the originality of bespoke building. And the fact that the builder is registered.

Business

Dale Morvick Builders
Ph. 021583917
58 Harlow Rd Kerrigan Bay Auckland 0915
PO Box 287 Tawharu 0563

```html
<!DOCTYPE html>
<html lang="en">
<head>
<meta charset="utf-8">
<title>Harbourline Homes – Business Card</title>
<link rel="stylesheet" href="https://fonts.googleapis.com/css2?family=PT+Sans:wght@400;700&display=swap">
<style>
  :root {
    --backdrop: #2f2a27;
    --card-dark: #1d1d1e;
    --card-red-light: #c63c2e;
    --card-red-deep: #b51b24;
    --brand-red: #c8232b;
    --text-light: #e6e6e6;
    --white: #ffffff;
  }
  * { margin: 0; padding: 0; box-sizing: border-box; }
  html, body {
    width: 1200px; height: 844px; overflow: hidden;
    background: var(--backdrop);
    font-family: "PT Sans", Arial, sans-serif;
  }
  .stage {
    position: relative; width: 1200px; height: 844px;
    display: flex; align-items: center; justify-content: center; gap: 50px;
  }
  .card {
    width: 525px; height: 300px; position: relative; overflow: hidden;
    box-shadow: 0 14px 30px rgba(0,0,0,0.45);
  }
  .card--back { background: var(--card-dark); }
  .card--front {
    background: linear-gradient(120deg, var(--card-red-light), var(--card-red-deep));
    display: flex; align-items: center; justify-content: center;
  }
  .brand {
    display: flex; align-items: center; gap: 8px;
    font-weight: 700; line-height: 1; white-space: nowrap;
  }
  .brand__square { width: 12px; height: 12px; flex: none; }
  .card--back .brand {
    position: absolute; left: 30px; top: 150px;
    color: var(--brand-red); font-size: 22px;
  }
  .card--back .brand__square { background: var(--brand-red); }
  .card--front .brand { color: var(--white); font-size: 50px; gap: 16px; }
  .card--front .brand__square { background: var(--white); width: 22px; height: 22px; }
  .divider {
    position: absolute; left: 270px; top: 72px; width: 1px; height: 156px;
    background: linear-gradient(to bottom, transparent, var(--brand-red), transparent);
  }
  .contact {
    position: absolute; left: 292px; top: 80px;
    color: var(--text-light); font-size: 14px; line-height: 1.45; white-space: nowrap;
  }
  .contact__name {
    color: var(--brand-red); font-size: 16px; font-weight: 700; margin-bottom: 12px;
  }
  .contact__phone { display: flex; align-items: center; gap: 8px; margin-bottom: 12px; }
  .contact__phone svg { width: 12px; height: 12px; fill: var(--brand-red); }
</style>
</head>
<body>
  <main class="stage">
    <section class="card card--back" aria-label="Card back with contact details">
      <div class="brand"><span class="brand__square"></span><span class="brand__name">Harbourline Homes</span></div>
      <div class="divider"></div>
      <div class="contact">
        <p class="contact__name">Dale Morvick Builders</p>
        <p class="contact__phone">
          <svg viewBox="0 0 24 24" aria-hidden="true"><path d="M6.6 10.8a15.1 15.1 0 0 0 6.6 6.6l2.2-2.2a1 1 0 0 1 1-.25 11.4 11.4 0 0 0 3.6.57 1 1 0 0 1 1 1V20a1 1 0 0 1-1 1A17 17 0 0 1 3 4a1 1 0 0 1 1-1h3.5a1 1 0 0 1 1 1c0 1.25.2 2.45.57 3.57a1 1 0 0 1-.25 1z"/></svg>
          <span>021583917</span>
        </p>
        <p class="contact__address">58 Harlow Rd Kerrigan Bay<br>Auckland 0915<br>PO Box 287 Tawharu 0563</p>
      </div>
    </section>
    <section class="card card--front" aria-label="Card front with company name">
      <div class="brand"><span class="brand__square"></span><span class="brand__name">Harbourline Homes</span></div>
    </section>
  </main>
</body>
</html>
```